Yoga site design

we need to design a homepage and content sections for our yoga portal

Verandel

Verandel is a yoga community ecosystem dedicated to the yoga enthusiasts and adopters of an active lifestyle based upon yoga and ayurvedic living. The objective of Verandel is to expand the involvment and adoption of yoga across the communities and facilitate the profitable growth of the various stakeholders and service providers involved with the ecosystem

Site descriptor

The site will have 4 building blocks/functionalities as specified below;

1.Directory functionality wherein it would list yoga classes/events/ workshop/ retreats and show calendar by dates and place
1. when
2. where
3. what
4. who
5. cost
6. durations

2.Search functionality

a.Find a yoga class/studio close to you (location tagging/google maps)
search/show by studioname/ teacher/ Private sessions/ yoga family
1. when
2. where
3. what
4. who
5. cost

3.Content publishing capabilty

a.Micro sites studio directory/ teachers/ frequent event holders/ therapists - contributors and serviceproviders
1. words of descriprion about yourself and your business
2. an email address
3. a live web link
4. google maps
5. contact phone number
6. a logo upload
7. a picture of themselves, (we need to specify size)
8 Weekly/monthly calendar - where thay are and when

b.Topical content
• columns written by a refference or celebrity
• parts in Montly newsletter and/or downloadable

c.Monthly Newsletter

d.What is New/News/Flash Happenings on the Site

e.Community Board
a virtual meeting place on a login and username basis
• Chirper
• chat
• yoganetwork - offline community build
• find a group close to you!

4.E-commerce capability (Yoga store)
by category;
• yoga props
• yoga clothes
• Ayurvedic related products
• Books/Music/dvd
• skin/body
tickets to events -
Updates

Reason: not enough iterations

Reason: i was unwell for the last two weeks

Target Market(s)

yoga enthusiasts across multiple cities in europe and americas

Industry/Entity Type

Building

Requirements
Must have
• the design should not be intrusive and allow for multiple city instances to be created using the same deisgn sensibilities
Should not have
• i do not need any tech coding.

```html
<!DOCTYPE html>
<html lang="en">
<head>
<meta charset="utf-8">
<title>Verandel – Yoga Community</title>
<link href="https://fonts.googleapis.com/css2?family=Arimo:ital,wght@0,400;0,700;1,700&display=swap" rel="stylesheet">
<style>
:root{
  --green-dark:#1f6b12;
  --green:#2f8a1c;
  --green-bright:#3c9d22;
  --green-text:#2b8a12;
  --accent:#22c21f;
  --nav:#1e7a2b;
  --nav-active:#0f4f1e;
  --hero:#2c2a28;
  --footer:#262321;
  --panel-border:#cfd2c7;
  --text:#222;
  --muted:#8a8a8a;
  --page-top:#eef3c9;
  --page-bottom:#fbfce9;
}
*{box-sizing:border-box;margin:0;padding:0}
html,body{width:919px;height:1200px;overflow:hidden}
body{font-family:Arimo,Arial,sans-serif;color:var(--text);position:relative;background:linear-gradient(var(--page-top),var(--page-bottom) 60%,#f4f6dc)}
.abs{position:absolute}

/* header */
.header{left:0;top:0;width:919px;height:89px;background:linear-gradient(#6ab33b,#3c8f22 60%,#2e7a18)}
.brand{left:96px;top:14px;display:flex;align-items:center;gap:12px;color:#fff;font-weight:700;font-size:30px}
.brand-mark{width:40px;height:40px;border-radius:50%;background:#e3efd8}
.topbar{left:404px;top:0;width:407px;height:24px;background:#e8eae3;display:flex;align-items:center;font-size:9px;font-weight:700;color:#333;padding-left:12px;gap:14px}
.topbar span::before{content:"";display:inline-block;width:7px;height:7px;background:#333;margin-right:4px;vertical-align:-1px}
.search{margin-left:auto;width:130px;height:24px;background:#f6f6f3;color:#888;font-weight:400;padding:7px 8px}
.search-btn{width:24px;height:24px;background:#222;display:flex;align-items:center;justify-content:center}
.call{left:600px;top:38px;color:#e8f4de;font-size:15px;font-style:italic;font-weight:700;display:flex;align-items:center;gap:10px}

.nav{left:0;top:89px;width:919px;height:44px;background:linear-gradient(#2b8a37,#1a6a26);display:flex;padding-left:96px;border-top:1px solid #0f5a1c}
.nav a{color:#fff;font-size:12px;font-weight:700;text-decoration:none;display:flex;align-items:center;justify-content:center;border-right:1px solid #4ea85a;height:44px}
.nav a.active{background:var(--nav-active)}

.hero{left:0;top:133px;width:919px;height:267px;background:radial-gradient(ellipse at 40% 40%,#45423f,var(--hero) 70%)}
.hero-text{left:133px;top:198px;width:245px;color:#fff;font-size:16px;font-weight:700;font-style:italic;line-height:26px}
.hero-text em{color:var(--accent)}
.hero-photo{left:387px;top:147px;width:426px;height:240px;background:#fff;padding:6px}
.hero-photo div{width:100%;height:100%;background:linear-gradient(170deg,#cfe8f5 0%,#b8dd7a 35%,#6fbf2a 70%,#3f8f1a 100%)}

/* panels */
.panel{background:#fff;border:1px solid var(--panel-border);border-radius:3px;box-shadow:0 1px 2px rgba(0,0,0,.08)}
.panel-title{font-size:16px;font-weight:700;font-style:italic;color:var(--green-text)}
.dark-title{font-size:16px;font-weight:700;font-style:italic;color:#222}

.chat{left:96px;top:409px;width:200px;height:40px;display:flex;align-items:center;gap:8px;padding-left:8px}
.chat-title{font-size:19px;font-weight:700;font-style:italic;color:var(--green-dark)}

.calendar{left:96px;top:456px;width:200px;height:180px;padding:4px 6px}
.calendar h3{font-size:13px;margin-bottom:6px}
.cal-grid{display:grid;grid-template-columns:repeat(7,1fr);row-gap:3px;text-align:center;font-size:13px;font-weight:700}
.cal-grid .o{color:#c8c8c8}
.cal-grid .h{background:#e3e3e3}
.cal-grid .d{font-size:9px;color:#aaa;font-weight:400}
.cal-grid .d.s{color:#e33}

.signup{left:96px;top:644px;width:200px;height:107px;padding:8px}
.signup .email{margin-top:12px;height:22px;border:1px solid #ccc;font-size:9px;color:#aaa;font-style:italic;padding:5px 6px;background:#f8f8f8}
.btn-submit{margin:10px 0 0 auto;width:76px;height:22px;background:linear-gradient(#4aa82a,#226b10);color:#fff;font-weight:700;font-style:italic;font-size:13px;text-align:center;line-height:22px}

.events{left:96px;top:760px;width:200px;height:220px;padding:8px 0}
.events h3{padding-left:8px;margin-bottom:10px}
.event{display:flex;gap:10px;padding:16px 8px 14px;border-bottom:1px solid #e2e2e2}
.event-ico{width:18px;height:18px;border:1px solid #c33;border-top:5px solid #d33;font-size:7px;text-align:center;flex:none;margin-top:6px}
.event b{display:block;color:var(--green-text);font-size:12px;line-height:14px}
.event small{color:#aaa;font-size:9px}
.ev-nav{display:flex;gap:8px;padding:14px 8px 0;align-items:center}
.arrow-btn{width:32px;height:20px;border-radius:4px;background:linear-gradient(#f4f4f4,#cfcfcf);border:1px solid #aaa;display:flex;align-items:center;justify-content:center}
.view-more{margin-left:auto;color:#999;font-size:12px;font-weight:700}

.member{left:96px;top:990px;width:200px;height:63px;background:linear-gradient(#2f8a1c,#4aa82a);color:#fff;padding:8px 10px}
.member b{font-size:13px;display:block;margin-bottom:4px}
.member p{font-size:9px;line-height:12px}

.social{left:96px;top:1063px;width:200px;height:47px;background:#f3f3ee;font-size:10px;color:#555}
.social div{display:flex;align-items:center;gap:5px;padding:3px 6px;border-bottom:1px solid #ddd;height:20px}
.social i{display:inline-block;width:11px;height:11px;background:#4a68a8}
.social i.c{background:#3aa8dd}

.welcome{left:304px;top:411px;width:507px;height:366px;padding:12px 12px}
.welcome h2{font-size:16px;color:var(--green-dark);margin-bottom:6px}
.welcome p{font-size:8.5px;line-height:14px;text-align:justify}
.welcome h4{margin-top:22px;font-size:11px;color:#777}
.welcome ul{margin-top:12px;padding-left:12px;font-size:8.5px;line-height:14px}
.welcome li{margin-bottom:12px}
.welcome h2.store{margin-top:8px;color:var(--green-dark)}
.store-grid{display:grid;grid-template-columns:repeat(3,152px);gap:9px 10px;margin-top:8px}
.store-grid div{height:35px;background:linear-gradient(#43a52a,#1f7a13);color:#fff;font-weight:700;font-size:16px;display:flex;align-items:center;justify-content:center}

.schedule{left:304px;top:788px;width:507px;height:256px;padding:10px 12px}
.schedule h3{font-size:14px;color:var(--green-dark)}
.days{font-size:10px;color:#777;margin-top:10px}
.days b{color:#222}
.today{font-size:10px;color:#777;font-weight:700;margin-top:12px}
.centers{position:absolute;right:16px;top:40px;width:100px;height:22px;border-radius:3px;background:linear-gradient(#dedede,#bdbdbd);font-size:11px;font-weight:700;color:#333;display:flex;align-items:center;padding-left:10px;gap:10px}
.rows{position:absolute;left:14px;top:86px;width:453px}
.row{display:flex;align-items:center;height:19px;margin-bottom:3.7px;background:#eeeeee;font-size:8.5px}
.row .tag{width:41px;height:19px;background:var(--green-dark);color:#fff;font-weight:700;font-size:10px;display:flex;align-items:center;justify-content:center}
.row.alt .tag{background:#aaa}
.row .time{margin-left:12px;width:80px}
.row .cls{width:118px;color:var(--green-dark);font-weight:700;font-size:10px}
.row.alt .cls{color:#aaa}
.row .lorem{width:125px;color:var(--green-dark)}
.row .res{color:var(--green-dark)}
.scrollbar{position:absolute;left:474px;top:86px;width:16px;height:155px;background:#eee}
.scrollbar div{width:16px;height:16px;margin-top:12px;background:var(--green-dark)}

.center{left:312px;top:1055px;width:499px}
.center h3{font-size:13px;margin-bottom:8px}
.center p{font-size:8.5px;line-height:13px}

.footer{left:0;top:1124px;width:919px;height:76px;background:var(--footer);color:#bbb;font-size:9.5px;display:flex;align-items:center;padding:0 108px 4px 100px}
.footer nav span{margin-right:8px}
.footer nav span+span::before{content:"|";margin-right:8px}
.footer .mail{margin-left:auto;font-weight:700}
</style>
</head>
<body>

<header class="abs header"></header>
<div class="abs brand"><span class="brand-mark"></span>Verandel</div>
<div class="abs topbar">
  <span>Schedule</span><span>Online Reservations</span><span>Membership</span>
  <div class="search">Search</div>
  <div class="search-btn"><svg width="6" height="8"><path d="M0 0L6 4L0 8Z" fill="#fff"/></svg></div>
</div>
<div class="abs call">
  <svg width="34" height="28" viewBox="0 0 34 28"><rect x="4" y="10" width="26" height="16" rx="3" fill="#d8dfe3" stroke="#556" /><path d="M2 9Q17 -2 32 9L28 12Q17 4 6 12Z" fill="#8a96a0"/><circle cx="17" cy="18" r="4" fill="#8a96a0"/></svg>
  Call us : +1 555 018 2040
</div>

<nav class="abs nav">
  <a class="active" style="width:77px">Home</a>
  <a style="width:78px">About us</a>
  <a style="width:90px">Yoga Classes</a>
  <a style="width:91px">Events</a>
  <a style="width:88px">Workshop</a>
  <a style="width:91px">Newletter</a>
  <a style="width:92px">Contact us</a>
</nav>

<section class="abs hero"></section>
<p class="abs hero-text">Verandel is a <em>yoga community</em> ecosystem dedicated to the yoga enthusiasts and adopters of an active lifestyle based upon <em>yoga and ayurvedic</em> living.</p>
<div class="abs hero-photo"><div role="img" aria-label="Photo of a person meditating in a sunlit green meadow"></div></div>

<aside>
  <div class="abs panel chat">
    <svg width="34" height="30" viewBox="0 0 34 30"><circle cx="12" cy="11" r="6" fill="#5fae3a"/><path d="M2 30Q2 18 12 18Q22 18 22 30Z" fill="#5fae3a"/><ellipse cx="26" cy="7" rx="8" ry="6" fill="#6cb4e8"/></svg>
    <span class="chat-title">24 x 7 Live Chat</span>
  </div>

  <div class="abs panel calendar">
    <h3>Calendar</h3>
    <div class="cal-grid">
      <span class="o">26</span><span class="o">27</span><span class="o">28</span><span class="o">29</span><span class="o">30</span><span class="h">1</span><span>2</span>
      <span>3</span><span>4</span><span>5</span><span>6</span><span>7</span><span class="h">8</span><span>9</span>
      <span>10</span><span>11</span><span>12</span><span>13</span><span>14</span><span class="h">15</span><span>16</span>
      <span>17</span><span>18</span><span>19</span><span>20</span><span>21</span><span class="h">22</span><span>23</span>
      <span>24</span><span>25</span><span>26</span><span>27</span><span>28</span><span class="h">29</span><span>30</span>
      <span>31</span><span class="o">1</span><span class="o">2</span><span class="o">3</span><span class="o">4</span><span class="o">5</span><span class="o">6</span>
      <span class="d s">S</span><span class="d">M</span><span class="d">T</span><span class="d">W</span><span class="d">T</span><span class="d">F</span><span class="d">S</span>
    </div>
  </div>

  <div class="abs panel signup">
    <div class="panel-title">Newletter Signup</div>
    <div class="email">Email</div>
    <div class="btn-submit">Submit</div>
  </div>

  <div class="abs panel events">
    <h3 class="dark-title">Upcoming Events</h3>
    <div class="event"><span class="event-ico">15</span><div><b>Lorem ipsum dolor sit ipsum Lorem ipsum</b><small>Sunday, August 30, 2011</small></div></div>
    <div class="event"><span class="event-ico">15</span><div><b>Lorem ipsum dolor sit ipsum Lorem ipsum</b><small>Sunday, August 30, 2011</small></div></div>
    <div class="ev-nav">
      <span class="arrow-btn"><svg width="10" height="8"><path d="M0 4L5 0V3H10V5H5V8Z" fill="#222"/></svg></span>
      <span class="arrow-btn"><svg width="10" height="8"><path d="M10 4L5 0V3H0V5H5V8Z" fill="#222"/></svg></span>
      <span class="view-more">View More..</span>
    </div>
  </div>

  <div class="abs member"><b>Member Monthly Newsletter</b><p>Find out about our monthly, annual and tax passes</p></div>

  <div class="abs social">
    <div><i></i>Join us on Circlebook</div>
    <div><i class="c"></i>Follow us on Chirper</div>
  </div>
</aside>

<main>
  <section class="abs panel welcome">
    <h2>Welcome &nbsp;to Verandel</h2>
    <p>Verandel is a yoga community ecosystem dedicated to the yoga enthusiasts and adopters of an active lifestyle based upon yoga and ayurvedic living. The objective of Verandel is to expand the involvment and adoption of yoga across the communities and facilitate the profitable growth of the various stakeholders and service providers involved with the ecosystem</p>
    <h4>Our Services</h4>
    <ul>
      <li>Lorem ipsum dolor sit ipsum Lorem ipsum dolor sit ipsum Lorem ipsum dolor sit ipsum Lorem ipsum dolor sit ipsum Lorem ipsum dolor sit ipsum Lorem ipsum dolor sit ipsum Lorem ipsum dolor sit ipsum</li>
      <li>Lorem ipsum dolor sit ipsum Lorem ipsum dolor sit ipsum Lorem ipsum dolor sit ipsum Lorem ipsum dolor sit ipsum Lorem ipsum dolor sit ipsum Lorem ipsum dolor sit ipsum Lorem ipsum dolor sit ipsum</li>
    </ul>
    <h2 class="store">Ecommerce Capability (E-Store)</h2>
    <div class="store-grid">
      <div>Yoga Props</div><div>Yoga Cloths</div><div>Aurvedic Products</div>
      <div>Books / Music / DVD</div><div>Skin / Body</div><div>Events Tickets</div>
    </div>
  </section>

  <section class="abs panel schedule">
    <h3>Upcoming Class Schedule</h3>
    <div class="days"><b>Sat</b> &nbsp;|&nbsp; Sun &nbsp;|&nbsp; Mon &nbsp;|&nbsp; Tue &nbsp;|&nbsp; Wed &nbsp;|&nbsp; Thu &nbsp;|&nbsp; Fri</div>
    <div class="today">Today Aug 30, 2011</div>
    <div class="centers">All Centers <svg width="12" height="8"><path d="M0 0H12L6 8Z" fill="#fff"/></svg></div>
    <div class="rows">
      <div class="row"><span class="tag">XYZ</span><span class="time">12:00 - 1.00 pm</span><span class="cls">XYZ</span><span class="lorem">Lorem Ipsum</span><span class="res">Reserve</span></div>
      <div class="row alt"><span class="tag">XYZ</span><span class="time">12:00 - 1.00 pm</span><span class="cls">XYZ</span><span class="lorem">Lorem Ipsum</span><span class="res">Reserve</span></div>
      <div class="row"><span class="tag">XYZ</span><span class="time">12:00 - 1.00 pm</span><span class="cls">XYZ</span><span class="lorem">Lorem Ipsum</span><span class="res">Reserve</span></div>
      <div class="row alt"><span class="tag">XYZ</span><span class="time">12:00 - 1.00 pm</span><span class="cls">XYZ</span><span class="lorem">Lorem Ipsum</span><span class="res">Reserve</span></div>
      <div class="row"><span class="tag">XYZ</span><span class="time">12:00 - 1.00 pm</span><span class="cls">XYZ</span><span class="lorem">Lorem Ipsum</span><span class="res">Reserve</span></div>
      <div class="row alt"><span class="tag">XYZ</span><span class="time">12:00 - 1.00 pm</span><span class="cls">XYZ</span><span class="lorem">Lorem Ipsum</span><span class="res">Reserve</span></div>
      <div class="row"><span class="tag">XYZ</span><span class="time">12:00 - 1.00 pm</span><span class="cls">XYZ</span><span class="lorem">Lorem Ipsum</span><span class="res">Reserve</span></div>
    </div>
    <div class="scrollbar"><div></div></div>
  </section>

  <section class="abs center">
    <h3>Find your Center</h3>
    <p>Feel great in mind, body, and soul. Learn how yoga can contribute to your healthy living at Verandel. Our foundation classes are a great way to find the style of yoga that's best for you<br>Discover Benefits &gt;</p>
  </section>
</main>

<footer class="abs footer">
  <nav><span>Home</span><span>About us</span><span>Yoga Classes</span><span>Events</span><span>Workshop</span><span>Newletter</span><span>Contact us</span></nav>
  <span class="mail">Email address : XXXXXXXXXXXXXXXXXXX</span>
</footer>

</body>
</html>
```